" Brigadeiros Veganos artesanais que são vendidos apenas em pontos de vendas veganos, não são vendidos para clientes finais diretamente. Negócio B2B. "

```html
<!DOCTYPE html>
<html lang="pt-BR">
<head>
<meta charset="UTF-8">
<title>Delicê – Embalagem Brigaveg</title>
<link rel="stylesheet" href="https://fonts.googleapis.com/css2?family=Lilita+One&family=Kalam:wght@700&family=Nunito:wght@600;800&display=swap">
<style>
  :root {
    --wine: #8e0f18;
    --wine-dark: #5e0810;
    --red: #b3121e;
    --yellow: #ffd21a;
    --orange: #f08a00;
    --white: #ffffff;
    --cocoa: #3b1a0c;
    --cocoa-light: #6e3415;
    --stage: #eceae6;
  }
  * { box-sizing: border-box; margin: 0; padding: 0; }
  html, body { width: 1200px; height: 1200px; overflow: hidden; }
  body {
    background: var(--stage);
    font-family: "Nunito", sans-serif;
    position: relative;
  }
  .panel {
    position: absolute;
    background: radial-gradient(ellipse at 40% 40%, var(--red) 0%, var(--wine) 60%, var(--wine-dark) 100%);
    overflow: hidden;
  }
  .panel--lid { left: 330px; top: 130px; width: 760px; height: 400px; }
  .panel--front { left: 330px; top: 540px; width: 760px; height: 470px; }
  .panel--end { left: 110px; top: 540px; width: 210px; height: 470px; }

  .brand {
    position: absolute;
    display: flex;
    flex-direction: column;
    align-items: flex-start;
  }
  .brand__row { display: flex; align-items: center; gap: 12px; }
  .brand__dot { border-radius: 50%; background: var(--white); flex: none; }
  .brand__name {
    font-family: "Lilita One", sans-serif;
    color: var(--white);
    line-height: 1;
    letter-spacing: 1px;
  }
  .brand__tagline {
    font-family: "Nunito", sans-serif;
    font-weight: 600;
    color: var(--white);
    opacity: .9;
    margin-top: 4px;
    white-space: nowrap;
  }

  .brand--lid { left: 60px; top: 120px; }
  .brand--lid .brand__dot { width: 26px; height: 26px; }
  .brand--lid .brand__name { font-size: 86px; }
  .brand--lid .brand__tagline { font-size: 16px; margin-left: 40px; }

  .brand--front { left: 250px; top: 60px; }
  .brand--front .brand__dot { width: 30px; height: 30px; }
  .brand--front .brand__name { font-size: 104px; }
  .brand--front .brand__tagline { font-size: 18px; margin-left: 44px; }

  .brand--end { left: 20px; top: 240px; }
  .brand--end .brand__dot { width: 16px; height: 16px; }
  .brand--end .brand__name { font-size: 52px; }
  .brand--end .brand__tagline { font-size: 10px; margin-left: 28px; }

  .product-photo {
    position: absolute;
    left: 420px; top: 20px;
    width: 320px; height: 240px;
    background: linear-gradient(180deg, var(--cocoa-light) 0%, var(--cocoa) 60%, var(--orange) 100%);
  }
  .product-label {
    position: absolute;
    font-family: "Lilita One", sans-serif;
    color: var(--yellow);
    line-height: 1;
    white-space: nowrap;
  }
  .product-label--lid { left: 430px; top: 290px; font-size: 68px; }
  .product-label--end { left: 20px; top: 40px; font-size: 38px; }

  .slogan {
    position: absolute;
    left: 120px; top: 250px;
    width: 620px;
    font-family: "Kalam", cursive;
    font-weight: 700;
    color: var(--white);
    font-size: 46px;
    line-height: 1.1;
    transform: rotate(-6deg);
    text-align: center;
  }

  .chocolate-splash {
    position: absolute;
    left: 0; bottom: 0;
    width: 210px; height: 150px;
    background: linear-gradient(180deg, var(--cocoa-light) 0%, var(--cocoa) 100%);
  }
</style>
</head>
<body>
  <section class="panel panel--lid" aria-label="Tampa da embalagem">
    <div class="brand brand--lid">
      <div class="brand__row">
        <span class="brand__dot"></span>
        <span class="brand__name">Delicê</span>
      </div>
      <span class="brand__tagline">Doces Artesanais Veganos</span>
    </div>
    <div class="product-photo" role="img" aria-label="Foto de um brigadeiro vegano com granulado de chocolate em forminha laranja"></div>
    <div class="product-label product-label--lid">Brigaveg</div>
  </section>

  <section class="panel panel--end" aria-label="Lateral da embalagem">
    <div class="product-label product-label--end">Brigaveg</div>
    <div class="brand brand--end">
      <div class="brand__row">
        <span class="brand__dot"></span>
        <span class="brand__name">Delicê</span>
      </div>
      <span class="brand__tagline">Doces Artesanais Veganos</span>
    </div>
    <div class="chocolate-splash" role="img" aria-label="Foto de respingo de chocolate derretido"></div>
  </section>

  <section class="panel panel--front" aria-label="Frente da embalagem">
    <div class="brand brand--front">
      <div class="brand__row">
        <span class="brand__dot"></span>
        <span class="brand__name">Delicê</span>
      </div>
      <span class="brand__tagline">Doces Artesanais Veganos</span>
    </div>
    <p class="slogan">Ser Vegano &nbsp;Saudável<br>e também muito gostoso!</p>
  </section>
</body>
</html>
```